INTRODUCING - BRINDLE MOTOR CENTRE

WE WOULD LIKE TO TIDY UP OUR INTRODUCTION TO OUR COMPANY
WE NEED THE WORDING TO BE SIMILAR WITH our web page
https://brindlemotorcentre.example.nz/services/

this needs to be more concise with pictures added THAT TIE IN WITH EXPLAINATIONS

```html
<!DOCTYPE html>
<html lang="en">
<head>
<meta charset="utf-8">
<title>Brindle Motor Centre – Brake &amp; Clutch Specialists</title>
<link rel="stylesheet" href="https://fonts.googleapis.com/css2?family=Montserrat:wght@300;400;500;600;700;800&display=swap">
<style>
  :root {
    --yellow: #ffdc00;
    --ink: #161616;
    --header-dark: #1b1b1b;
    --body-text: #3a3a3a;
    --white: #ffffff;
    --rule: #c9c9c9;
  }
  * { box-sizing: border-box; margin: 0; padding: 0; }
  html, body { width: 783px; height: 1200px; overflow: hidden; background: var(--white); }
  body { font-family: "Montserrat", Arial, sans-serif; color: var(--body-text); }
  .flyer { position: relative; width: 783px; height: 1200px; overflow: hidden; background: var(--white); }

  /* Header */
  .hero { position: absolute; left: 0; top: 0; width: 783px; height: 430px;
    background: radial-gradient(ellipse at 30% 20%, #3a3a3a 0%, #202020 45%, #111 100%); overflow: hidden; }
  .hero-art { position: absolute; inset: 0; }
  .hero-edge { position: absolute; left: 0; bottom: 0; width: 783px; height: 5px; background: var(--ink); }
  .brand-box { position: absolute; left: 48px; top: 40px; width: 146px; height: 115px; background: var(--yellow);
    display: flex; align-items: center; justify-content: center; text-align: center; padding: 10px; }
  .brand-name { font-weight: 800; font-size: 17px; line-height: 1.2; color: var(--ink); letter-spacing: 0.5px; }
  .hero-title { position: absolute; left: 48px; top: 186px; color: var(--white); }
  .hero-title .line-light { display: block; font-weight: 300; font-size: 37px; letter-spacing: -0.5px; line-height: 40px; }
  .hero-title .line-bold { display: block; font-weight: 800; font-size: 33px; line-height: 40px; letter-spacing: -0.5px; }
  .hero-title .line-accent { display: block; font-weight: 800; font-size: 46px; line-height: 52px; color: var(--yellow); letter-spacing: -0.5px; }
  .hero-divider { position: absolute; left: 48px; top: 334px; width: 275px; height: 1px; background: #555; }
  .hero-divider::before { content: ""; position: absolute; left: 43px; top: -3px; width: 67px; height: 7px; border-radius: 4px; background: var(--yellow); }
  .hero-aim { position: absolute; left: 48px; top: 352px; width: 290px; color: var(--white); font-weight: 500; font-size: 15px; line-height: 19px; }

  /* Services */
  .services-title { position: absolute; left: 0; top: 455px; width: 783px; text-align: center; font-size: 31px; color: var(--ink); font-weight: 400; letter-spacing: -0.5px; }
  .services-title strong { font-weight: 800; }
  .services-rule { position: absolute; left: 254px; top: 499px; width: 275px; height: 1px; background: var(--rule); }
  .services-rule::before { content: ""; position: absolute; left: 112px; top: -3px; width: 51px; height: 6px; border-radius: 3px; background: var(--yellow); }

  .service-heading { position: absolute; font-weight: 600; font-size: 16px; color: var(--ink); letter-spacing: 0.3px; }
  .sub-heading { position: absolute; font-weight: 700; font-size: 12.5px; color: var(--ink); }
  .service-copy { position: absolute; font-size: 12px; line-height: 14.6px; color: var(--body-text); }

  .photo { position: absolute; border: 3px solid var(--white); box-shadow: 0 1px 5px rgba(0,0,0,0.35); }
  .photo-cable { left: 259px; top: 531px; width: 106px; height: 121px; background: linear-gradient(90deg, #0d0d0d, #4a4d52 20%, #111 40%, #45484d 60%, #0f0f0f 80%, #3b3d41); }
  .photo-caliper { left: 257px; top: 836px; width: 110px; height: 138px; background: radial-gradient(circle at 50% 55%, #8c8c88 0%, #b9a56a 25%, #e7e7e7 55%, #fafafa 100%); }
  .photo-parts { left: 621px; top: 516px; width: 118px; height: 122px; background: linear-gradient(90deg, #6b4a2e, #b7b0a4 35%, #e9e4da 50%, #a38465 65%, #5b3c24); }
  .photo-hoses { left: 621px; top: 801px; width: 118px; height: 134px; background: linear-gradient(160deg, #4a90b8 0%, #9aa4a8 35%, #c89a82 60%, #2d4e5f 100%); }

  .tick-list { position: absolute; list-style: none; font-weight: 600; font-size: 12.3px; line-height: 17.2px; color: var(--ink); }
  .tick-list li { position: relative; padding-left: 19px; }
  .tick-list li::before { content: ""; position: absolute; left: 0; top: 3.5px; width: 10px; height: 10px; border-radius: 50%; background: #d9b800; }
  .tick-list li::after { content: ""; position: absolute; left: 3.3px; top: 5.3px; width: 2.6px; height: 4.4px; border: solid var(--white); border-width: 0 1.4px 1.4px 0; transform: rotate(45deg); }
  .tick-list .wrap { line-height: 13.5px; padding-top: 2px; }

  /* Footer */
  .contact-bar { position: absolute; left: 0; top: 1119px; width: 783px; height: 81px; background: var(--ink);
    display: flex; align-items: center; justify-content: center; gap: 14px; padding: 0 10px 0 54px; color: var(--white); }
  .contact-bar::before { content: ""; position: absolute; left: 0; top: 0; width: 48px; height: 81px; background: var(--yellow); clip-path: polygon(0 0, 55% 0, 100% 100%, 0 100%); }
  .contact-item { display: flex; align-items: center; gap: 5px; font-weight: 600; font-size: 12px; white-space: nowrap; }
  .contact-item.phone { font-size: 17px; font-weight: 700; }
  .contact-item svg { flex: none; }
</style>
</head>
<body>
<main class="flyer">

  <header class="hero">
    <svg class="hero-art" width="783" height="430" viewBox="0 0 783 430">
      <defs>
        <linearGradient id="caliperTone" x1="0" y1="0" x2="1" y2="1">
          <stop offset="0" stop-color="#5a5f63"/>
          <stop offset="0.45" stop-color="#b9bcbd"/>
          <stop offset="0.75" stop-color="#7d8184"/>
          <stop offset="1" stop-color="#2f3234"/>
        </linearGradient>
      </defs>
      <polygon points="548,0 783,0 783,430 332,430" fill="url(#caliperTone)" role="img" aria-label="Close-up photo of a brake caliper housing on a workbench"/>
      <polygon points="530,0 548,0 332,430 314,430" fill="var(--yellow)"/>
    </svg>

    <div class="brand-box"><span class="brand-name">BRINDLE MOTOR CENTRE</span></div>

    <h1 class="hero-title">
      <span class="line-light">NEWZELAND’S</span>
      <span class="line-bold">BRAKE &amp; CLUTCH</span>
      <span class="line-accent">SPECIALISTS</span>
    </h1>
    <div class="hero-divider"></div>
    <p class="hero-aim">Our aim is to repair or manufacture parts with the quickest turnaround time possible.</p>
    <div class="hero-edge"></div>
  </header>

  <h2 class="services-title">OUR <strong>SERVICES</strong></h2>
  <div class="services-rule"></div>

  <!-- Cables -->
  <h3 class="service-heading" style="left:49px; top:530px;">CABLES</h3>
  <p class="service-copy" style="left:49px; top:552px; width:200px;">At Brindle Motor Centre we design, manufacture &amp; distribute specially engineered cables for a wide range of customers including marine, agriculture, lawn care, trucking, heavy lifting &amp; recreational vehicle.</p>
  <div class="photo photo-cable" role="img" aria-label="Photo of a reel of black cable"></div>
  <ul class="tick-list" style="left:49px; top:674px;">
    <li>Hand Brake</li><li>Clutch Cable</li><li>Motor Cycle</li><li>Marine</li>
    <li>Throttle</li><li>Gear Shifter Cables</li><li>Transmission</li>
  </ul>
  <ul class="tick-list" style="left:210px; top:674px;">
    <li>Excavator</li><li>Push Pull</li><li>Agricultural</li><li>Marine</li>
    <li>Remote Cable Controls</li><li>Speedo Cables</li>
  </ul>

  <!-- Brakes -->
  <h3 class="service-heading" style="left:49px; top:816px;">BRAKES</h3>
  <p class="service-copy" style="left:49px; top:842px; width:195px;">Brindle Motor Centre specialise in the repair of all brake components including resleeving cylinders, boosters, calipers, proportioning valves &amp; brake linings.</p>
  <p class="service-copy" style="left:49px; top:944px; width:200px;">All our resleeving is carried out using seamless stainless steel.</p>
  <div class="photo photo-caliper" role="img" aria-label="Photo of a rebuilt brake caliper"></div>
  <ul class="tick-list" style="left:49px; top:993px;">
    <li>Stainless Steel Resleeving</li><li>Brake Caliper Rebuilds</li><li>Booster Reconditioning</li>
    <li>Exchange Cylinders available</li><li>Cost Effective saving time and money</li>
    <li>Disc Caliper Pistons – Resleeved or Manufactured</li>
  </ul>

  <!-- Parts -->
  <h3 class="service-heading" style="left:423px; top:530px;">PARTS</h3>
  <p class="service-copy" style="left:423px; top:552px; width:185px;">Here at Brindle Motor Centre we hold an extensive range of specialised parts for all your brake requirements. We specialise in the “hard to get” parts.</p>
  <div class="photo photo-parts" role="img" aria-label="Photo of a parts warehouse aisle with stocked shelves"></div>
  <ul class="tick-list" style="left:423px; top:656px;">
    <li>Flywheel Machining</li><li>Commercial Wheel Cylinders</li><li>Brake Hoses</li>
    <li>Disc Rotors</li><li>Disc Pads</li><li>Brake Shoes</li><li>Brake Shoe Rebonding</li>
  </ul>
  <ul class="tick-list" style="left:634px; top:656px;">
    <li>Clutch Parts</li><li>Brake Piping</li><li>CV Joints</li><li>Brake Fluid</li>
    <li class="wrap">Stopclean Parts<br>Cleaner</li>
  </ul>

  <!-- Hoses -->
  <h3 class="service-heading" style="left:423px; top:797px;">HOSES</h3>
  <p class="service-copy" style="left:423px; top:820px; width:190px;">Brindle Motor Centre have been manufacturing brake hoses for more than 15 years. The hose and end fittings that we have in stock should enable us to supply brake hoses for up to 90% of the vehicles on the road today.</p>
  <div class="photo photo-hoses" role="img" aria-label="Photo of a technician crimping a brake hose fitting"></div>
  <h4 class="sub-heading" style="left:423px; top:958px;">Automotive Hoses</h4>
  <p class="service-copy" style="left:423px; top:977px; width:320px;">Brindle Motor Centre make on site, Power Steering hoses, Fuel hoses, etc., for any application needed on your vehicle.</p>
  <h4 class="sub-heading" style="left:423px; top:1035px;">Braided Hoses</h4>
  <p class="service-copy" style="left:423px; top:1056px; width:330px;">To compliment our Brake and Automotive hoses, Brindle Motor Centre can offer to have your hoses made in Braid for greater endurance and better look.</p>

  <!-- Contact -->
  <footer class="contact-bar">
    <span class="contact-item phone">
      <svg width="15" height="15" viewBox="0 0 24 24" aria-hidden="true"><path fill="var(--yellow)" d="M6.6 10.8a15.1 15.1 0 0 0 6.6 6.6l2.2-2.2a1 1 0 0 1 1-.25 11.4 11.4 0 0 0 3.6.57 1 1 0 0 1 1 1V20a1 1 0 0 1-1 1A17 17 0 0 1 3 4a1 1 0 0 1 1-1h3.5a1 1 0 0 1 1 1c0 1.25.2 2.45.57 3.57a1 1 0 0 1-.25 1z"/></svg>
      0800 555 014
    </span>
    <span class="contact-item">
      <svg width="15" height="12" viewBox="0 0 24 18" aria-hidden="true"><rect x="1" y="1" width="22" height="16" fill="none" stroke="var(--yellow)" stroke-width="2"/><path d="M1 1l11 9 11-9M1 17l8-7M23 17l-8-7" fill="none" stroke="var(--yellow)" stroke-width="2"/></svg>
      parts@brindlemotorcentre.example.nz
    </span>
    <span class="contact-item">
      <svg width="14" height="14" viewBox="0 0 24 24" aria-hidden="true"><g fill="none" stroke="var(--yellow)" stroke-width="2"><circle cx="12" cy="12" r="10"/><ellipse cx="12" cy="12" rx="4.5" ry="10"/><path d="M2 12h20M4 6.5h16M4 17.5h16"/></g></svg>
      www.brindlemotorcentre.example.nz
    </span>
  </footer>

</main>
</body>
</html>
```